Business Card Design

we are a Business Training & Consulting company that specializes in Lean Six Sigma coaching & consulting. Our clients are Big Businesses and Consultancy firms. Need a card design that is minimalist and elegant.. need to feature logo of our KRV brand & probably at the back we also need to include the logo of the parent company (DORAMBE Business Group Pty. Ltd.)
Font needs to be consistent with our website font especially the KRV font on the website header.. (www.krvqa.example)
Hi All,
Industry/Entity Type
Business
Contact Information for Business Card
Marcus T Ellingrove
Director
Business Consultancy & Training Programs
www.krvqa.example
P.O. Box 5172,
Perth, Western Australia, 6164, Australia.
M: +61 4 5538 9071
T: 1 300 579 218
F: +61 8 9727 3185
marcus@krvqa.example
ABN # : 73 2951 807 36
ACN #: 295 180 736

```html
<!DOCTYPE html>
<html lang="en">
<head>
<meta charset="utf-8">
<title>KRV Training and Consultancy – Business Card</title>
<link rel="stylesheet" href="https://fonts.googleapis.com/css2?family=Open+Sans:wght@300;400;600&display=swap">
<style>
  :root {
    --stage: #1d3552;
    --white: #ffffff;
    --navy: #0f2d55;
    --ink: #14203a;
    --gold: #f2c94c;
    --cyan: #2cc3f0;
    --cyan-soft: #7fd9f5;
    --sky-deep: #16a6df;
    --brand-blue: #1f6fb5;
  }
  * { box-sizing: border-box; margin: 0; padding: 0; }
  html, body {
    width: 1200px; height: 846px; overflow: hidden;
    background: var(--stage);
    font-family: "Open Sans", Arial, sans-serif;
  }
  .stage {
    position: relative; width: 1200px; height: 846px;
    display: flex; align-items: center; justify-content: center; gap: 40px;
  }
  .card {
    position: relative; width: 540px; height: 308px; overflow: hidden;
    background: var(--white);
    box-shadow: 0 10px 30px rgba(0,0,0,.35);
  }

  /* Front */
  .front .band-navy { position: absolute; left: 0; right: 0; top: 110px; height: 122px; background: var(--navy); }
  .front .band-cyan { position: absolute; left: 0; right: 0; top: 232px; bottom: 0; background: var(--cyan); }
  .brand-mark {
    position: absolute; left: 28px; top: 44px;
    display: flex; align-items: center; gap: 8px;
  }
  .brand-mark .dot { width: 22px; height: 22px; border-radius: 50%; background: var(--gold); }
  .brand-mark .name { font-weight: 600; font-size: 26px; color: var(--navy); letter-spacing: 1px; }
  .title { position: absolute; left: 150px; top: 14px; color: var(--ink); font-weight: 400; line-height: 1.1; }
  .title .line-1 { font-size: 36px; letter-spacing: 1.5px; }
  .title .line-2 { font-size: 24px; letter-spacing: 1.5px; padding-left: 20px; font-weight: 300; }
  .person { position: absolute; left: 28px; top: 142px; }
  .person .name { color: var(--gold); font-size: 23px; font-weight: 400; }
  .person .role { color: var(--cyan); font-size: 12.5px; font-weight: 300; line-height: 1.35; margin-top: 4px; }
  .contact { position: absolute; left: 300px; top: 118px; list-style: none; color: var(--gold); font-size: 11.5px; line-height: 1.25; }
  .contact li { display: flex; gap: 8px; align-items: flex-start; margin-bottom: 3px; }
  .contact svg { flex: none; width: 12px; height: 12px; margin-top: 1px; }
  .registry { position: absolute; left: 322px; top: 238px; color: var(--navy); font-size: 11.5px; line-height: 1.3; }
  .front .web { position: absolute; left: 60px; top: 266px; color: var(--navy); font-size: 15px; letter-spacing: 3px; }

  /* Back */
  .back .sky { position: absolute; inset: 0; }
  .parent-mark { position: absolute; left: 0; right: 0; top: 108px; text-align: center; color: var(--brand-blue); font-weight: 600; }
  .parent-mark .name { font-size: 40px; letter-spacing: 2px; line-height: 1; }
  .parent-mark .sub { font-size: 12px; letter-spacing: .5px; margin-top: 6px; }
  .back .web { position: absolute; left: 0; right: 0; top: 222px; text-align: center; color: var(--navy); font-size: 15px; letter-spacing: 3px; }
</style>
</head>
<body>
<main class="stage">

  <section class="card front" aria-label="Card front">
    <div class="band-navy"></div>
    <div class="band-cyan"></div>

    <div class="brand-mark"><span class="dot"></span><span class="name">KRV</span></div>
    <h1 class="title"><div class="line-1">KRV TRAINING</div><div class="line-2">AND CONSULTANCY</div></h1>

    <div class="person">
      <div class="name">Marcus T Ellingrove</div>
      <div class="role">Director Business Consultancy<br>&amp; Training Programs</div>
    </div>

    <ul class="contact">
      <li>
        <svg viewBox="0 0 12 12"><rect width="12" height="12" rx="2" fill="#f2c94c"/><path d="M6 2.2a2.5 2.5 0 0 0-2.5 2.5C3.5 6.6 6 9.8 6 9.8s2.5-3.2 2.5-5.1A2.5 2.5 0 0 0 6 2.2z" fill="#0f2d55"/><circle cx="6" cy="4.7" r=".9" fill="#f2c94c"/></svg>
        <span>P.O. Box 5172, Perth,<br>Western Australia,<br>6164, Australia.</span>
      </li>
      <li>
        <svg viewBox="0 0 12 12"><rect width="12" height="12" rx="2" fill="#f2c94c"/><rect x="3.8" y="2" width="4.4" height="8" rx=".8" fill="#0f2d55"/><rect x="4.6" y="3" width="2.8" height="5" fill="#f2c94c"/></svg>
        <span>+61 4 5538 9071</span>
      </li>
      <li>
        <svg viewBox="0 0 12 12"><rect width="12" height="12" rx="2" fill="#f2c94c"/><path d="M3.5 2.5l1.6 1.6-.9 1.1a5 5 0 0 0 2.6 2.6l1.1-.9 1.6 1.6-1 1c-3 0-6-3-6-6z" fill="#0f2d55"/></svg>
        <span>1 300 579 218</span>
      </li>
      <li>
        <svg viewBox="0 0 12 12"><rect width="12" height="12" rx="2" fill="#f2c94c"/><rect x="2.5" y="5" width="7" height="4.5" fill="#0f2d55"/><rect x="4" y="2.5" width="4" height="3" fill="#0f2d55"/></svg>
        <span>+61 8 9727 3185</span>
      </li>
      <li>
        <svg viewBox="0 0 12 12"><rect width="12" height="12" rx="2" fill="#f2c94c"/><rect x="2.2" y="3.3" width="7.6" height="5.4" fill="#0f2d55"/><path d="M2.2 3.3L6 6.4l3.8-3.1" stroke="#f2c94c" stroke-width=".8" fill="none"/></svg>
        <span>marcus@krvqa.example</span>
      </li>
    </ul>

    <div class="registry">ABN # : 73 2951 807 36<br>ACN #: 295 180 736</div>
    <div class="web">www.krvqa.example</div>
  </section>

  <section class="card back" aria-label="Card back">
    <svg class="sky" viewBox="0 0 540 308" preserveAspectRatio="none" aria-hidden="true">
      <defs>
        <linearGradient id="skyFade" x1="0" y1="0" x2="0" y2="1">
          <stop offset="0" stop-color="#7fd9f5"/>
          <stop offset="1" stop-color="#16a6df"/>
        </linearGradient>
      </defs>
      <rect width="540" height="308" fill="#ffffff"/>
      <rect y="112" width="540" height="196" fill="url(#skyFade)"/>
      <rect x="120" y="88" width="300" height="120" rx="46" fill="#ffffff"/>
    </svg>
    <div class="parent-mark">
      <div class="name">DORAMBE</div>
      <div class="sub">Business Group Pty. Ltd.</div>
    </div>
    <div class="web">www.dorambe.example</div>
  </section>

</main>
</body>
</html>
```